Billboard design - consider what a billboard is

Design a billboard using my logo - Billboard is 6m x 3m
A Billboard is advertising for my company that is on a big sign.

Has to be clean and easy to read, and ideally highlights that we are Residential and Commercial builders.

Keep it clean and easy to read

The contact number for the board is

022 583 7092
www.harbourframeworks.co.nz
info@harbourframeworks.co.nz

Doesnt have to have all contact details if it doesnt fit

Has to catch peoples attention to contact us if they need a builder

Can you please change the sign to be all white writing, with black background ?
Updates

Please consider what a billboard is...

The design needs to be suitable for a billboard..

Target Market(s)

people driving past

Industry/Entity Type

Construction

Logo Text

Wellington Builder, website email address, contact number

Colors
0054AA
0677BA
7BADD7
CADEEF
E8F1F8

Requirements
Must have
• Easy to read
Nice to have
• easy to read, can clearly see contact details

```html
<!DOCTYPE html>
<html lang="en">
<head>
<meta charset="UTF-8">
<title>Harbour Frameworks Billboard</title>
<link rel="stylesheet" href="https://fonts.googleapis.com/css2?family=Montserrat:wght@600;700&display=swap">
<style>
  :root {
    --page: #ffffff;
    --board-blue: #1357a6;
    --accent-blue: #5a8dca;
    --panel-white: #ffffff;
    --text-light: #eaf2fa;
    --brand-blue: #5a8dca;
  }
  html, body {
    margin: 0;
    padding: 0;
    width: 1200px;
    height: 1200px;
    overflow: hidden;
    background: var(--page);
  }
  .canvas {
    position: relative;
    width: 1200px;
    height: 1200px;
    font-family: "Montserrat", Arial, sans-serif;
  }
  .billboard {
    position: absolute;
    left: 104px;
    top: 369px;
    width: 941px;
    height: 488px;
    background: var(--board-blue);
    overflow: hidden;
  }
  .billboard-shapes {
    position: absolute;
    inset: 0;
  }
  .brand-name {
    position: absolute;
    left: 67px;
    top: 208px;
    width: 240px;
    text-align: center;
    color: var(--brand-blue);
    font-weight: 700;
    font-size: 28px;
    line-height: 1.1;
    letter-spacing: 0.5px;
  }
  .copy {
    position: absolute;
    text-align: right;
    color: var(--text-light);
    white-space: nowrap;
    line-height: 1;
    margin: 0;
  }
  .headline {
    font-weight: 700;
    letter-spacing: 3px;
  }
  .headline-place { top: 56px; font-size: 64px; right: 41px; }
  .headline-trade { top: 121px; font-size: 67px; right: 37px; letter-spacing: 2px; }
  .services {
    font-weight: 700;
    font-size: 19px;
    letter-spacing: 1.4px;
  }
  .services-sectors { top: 201px; right: 41px; }
  .services-types { top: 232px; right: 34px; }
  .phone {
    top: 316px;
    right: 25px;
    font-weight: 700;
    font-size: 59px;
    letter-spacing: 0;
  }
  .web-address, .email-address {
    font-weight: 600;
    font-size: 24px;
    letter-spacing: 2px;
  }
  .web-address { top: 392px; right: 27px; }
  .email-address { top: 424px; right: 25px; }
</style>
</head>
<body>
<div class="canvas">
  <section class="billboard">
    <svg class="billboard-shapes" width="941" height="488" viewBox="0 0 941 488" aria-hidden="true">
      <polygon points="121,0 254,0 187,66" fill="var(--accent-blue)"/>
      <polygon points="113,488 262,488 187,413" fill="var(--accent-blue)"/>
      <polygon points="187,66 361,240 187,413 14,240" fill="var(--panel-white)"/>
    </svg>
    <div class="brand-name">HARBOUR<br>FRAMEWORKS</div>

    <h1 class="copy headline headline-place">WELLINGTON</h1>
    <h2 class="copy headline headline-trade">BUILDER</h2>
    <p class="copy services services-sectors">RESIDENTIAL &amp; COMMERCIAL CONSTRUCTION</p>
    <p class="copy services services-types">NEW BUILDS ● RENOVATIONS ● EXTENSIONS</p>
    <p class="copy phone">022 583 7092</p>
    <p class="copy web-address">www.harbourframeworks.co.nz</p>
    <p class="copy email-address">info@harbourframeworks.co.nz</p>
  </section>
</div>
</body>
</html>
```